Small boutique multi-family apartment developer needs premium website design.

We are a growing real estate development company specializing in multi family apartment development. Our company Mireval Stone Development focuses on passive real estate investors looking to maximize their current real estate portfolio by allowing us to develop and reposition their current properties allowing them more cashflow while we are also able to take over the management of their asset in order to ensure optimal performance on a consistent basis.

```html
<!DOCTYPE html>
<html lang="en">
<head>
<meta charset="utf-8">
<title>Mireval Stone Development</title>
<link rel="stylesheet" href="https://fonts.googleapis.com/css2?family=Poppins:wght@300;400;500;600;700&display=swap">
<style>
:root{
  --ink:#1d1f26;
  --text:#4a4a4f;
  --muted:#8a8a90;
  --accent:#c4a4a8;
  --accent-soft:#e6d6d8;
  --line:#e2dcdd;
  --paper:#ffffff;
  --panel:#f7f5f5;
  --navy:#23263a;
  --navy-line:#3a3d52;
}
*{box-sizing:border-box;margin:0;padding:0}
html,body{width:1200px;height:3062px;overflow:hidden;background:var(--paper)}
body{position:relative;font-family:'Poppins',sans-serif;color:var(--text)}
.abs{position:absolute}
a{color:inherit;text-decoration:none}

/* header */
.brand{left:191px;top:12px;height:42px;display:flex;align-items:center;gap:12px;color:var(--accent);font-size:13px;font-weight:400}
.brand-square{width:40px;height:40px;border:2px solid var(--accent)}
.nav{top:18px;height:30px;display:flex;align-items:center;font-size:10px;font-weight:400;color:var(--ink);letter-spacing:.3px}
.nav .current{left:651px;color:var(--muted);border-bottom:1px solid var(--accent);padding:2px 2px 4px}
.nav-link{font-size:10px;color:var(--ink)}
.btn-dark{left:893px;top:18px;width:97px;height:30px;background:var(--ink);color:#fff;font-size:10px;display:flex;align-items:center;justify-content:center;letter-spacing:.3px}

/* hero */
.hero{left:25px;top:67px;width:1133px;height:572px;background:linear-gradient(180deg,#5b6a55 0%,#3d4438 30%,#2b2c28 55%,#3f5231 78%,#27331f 100%)}
.hero-shade{left:25px;top:67px;width:1133px;height:572px;background:linear-gradient(90deg,rgba(0,0,0,.35),rgba(0,0,0,.05))}
.hero-frame{left:191px;top:243px;width:483px;height:396px;border-top:1px solid rgba(255,255,255,.55);border-left:1px solid rgba(255,255,255,.55);border-right:1px solid rgba(255,255,255,.25);border-bottom:none}
.hero-mark{left:210px;top:267px;width:24px;height:24px;border:1.5px solid #fff}
.hero-title{left:209px;top:300px;width:480px;color:#fff;font-size:25px;font-weight:500;line-height:32px}
.btn-ghost{display:flex;align-items:center;gap:8px;font-size:10px;letter-spacing:.3px}
.btn-ghost::before{content:"";width:10px;height:1px;background:currentColor}
.hero-btn{left:210px;top:422px;width:98px;height:29px;border:1px solid rgba(255,255,255,.8);color:#fff;padding-left:0}
.scroll-arrow{left:980px;top:596px}

/* section labels */
.label-line{left:25px;height:1px;width:240px;background:var(--accent-soft)}
.label{left:273px;font-size:10.5px;color:var(--accent);font-weight:300}
.heading{left:191px;color:var(--ink);font-size:23px;font-weight:500;line-height:27px}

/* about */
.about-rule{left:191px;top:820px;width:1px;height:320px;background:var(--line)}
.about-copy{left:209px;top:817px;width:368px;font-size:11.6px;line-height:21px;color:var(--text);text-align:justify}
.about-copy strong{color:var(--ink);font-weight:500}
.about-copy p+p{margin-top:21px}
.btn-outline{border:1px solid var(--line);color:var(--muted);justify-content:flex-start;padding-left:0}
.about-btn{left:209px;top:1051px;width:98px;height:29px}
.about-photo{left:643px;top:728px;width:349px;height:351px;background:linear-gradient(180deg,#1d3f8c 0%,#2c5bb0 35%,#4c5360 60%,#2d2a2a 100%)}
.about-inset{left:643px;top:728px;width:24px;height:351px;background:#1b2a66}
.about-tail{left:992px;top:1065px;width:166px;height:1px;background:var(--line)}

/* stats */
.stats-photo{left:25px;top:1141px;width:1133px;height:554px;background:linear-gradient(180deg,#9aa1b9 0%,#c6a9b2 30%,#7e7f91 55%,#6a5a4c 75%,#3a3f2b 100%)}
.stats-panel{left:191px;top:1547px;width:942px;height:123px;background:rgba(246,242,242,.92);display:flex}
.stat{flex:1;display:flex;flex-direction:column;align-items:center;justify-content:center;position:relative}
.stat+.stat::before{content:"";position:absolute;left:0;top:26px;height:52px;width:1px;background:var(--line)}
.stat-num{font-size:48px;font-weight:600;color:var(--accent);line-height:52px}
.stat-label{font-size:12px;color:var(--ink);margin-top:6px}

/* industry */
.card{top:1859px;width:254px;height:253px}
.card-1{left:191px;background:linear-gradient(160deg,#4a5563 0%,#2f3a45 60%,#5c6a72 100%)}
.card-2{left:464px;top:1856px;height:259px;background:linear-gradient(160deg,#7a7f84 0%,#4c5158 60%,#3e4550 100%);border-bottom:4px solid var(--accent)}
.card-3{left:737px;background:linear-gradient(160deg,#8b8f93 0%,#5f6a5d 55%,#6f747a 100%)}
.card-shade{position:absolute;inset:0;background:linear-gradient(180deg,rgba(0,0,0,0) 40%,rgba(0,0,0,.45) 100%)}
.card-num{position:absolute;left:18px;top:18px;font-size:17px;font-weight:600;color:var(--accent-soft)}
.card-title{position:absolute;left:18px;bottom:22px;color:#fff;font-size:19px;font-weight:500;line-height:22px}
.card-tail{left:991px;top:2079px;width:190px;height:1px;background:var(--line)}

/* properties */
.props-bg{left:25px;top:2174px;width:1133px;height:506px;background:var(--panel)}
.prop-photo{left:191px;top:2305px;width:470px;height:312px;background:linear-gradient(180deg,#1d3f8c 0%,#2f5ab0 40%,#4e5563 62%,#2a2727 100%)}
.prop-title{left:684px;top:2330px;font-size:19px;font-weight:500;color:var(--ink)}
.prop-desc{left:684px;top:2367px;width:308px;font-size:9.6px;line-height:15px;color:var(--text)}
.specs{left:684px;top:2411px;width:308px}
.spec{display:flex;align-items:center;height:25.5px;border-top:1px solid var(--line);font-size:9px;color:var(--ink);letter-spacing:.2px}
.spec-icon{width:9px;height:8px;border:1px solid var(--accent);margin-right:10px}
.spec span:last-child{margin-left:auto;font-weight:500}
.offered{left:684px;top:2531px;font-size:9.5px;color:var(--accent);line-height:13px}
.price{display:block;color:var(--ink);font-size:13px;font-weight:500;line-height:17px}
.prop-btn{left:893px;top:2533px;width:99px;height:29px;color:var(--accent)}
.prop-rule{left:274px;top:2617px;width:1px;height:63px;background:var(--line)}

/* footer */
.footer{left:25px;top:2680px;width:1133px;height:314px;background:var(--navy)}
.footer-sky{left:25px;top:2860px;width:1133px;height:134px;background:linear-gradient(180deg,rgba(255,255,255,0),rgba(255,255,255,.03))}
.footer-mark{left:191px;top:2708px;width:32px;height:32px;border:1.5px solid #fff}
.footer-nav{top:2720px;font-size:10px;color:#fff;letter-spacing:.2px}
.footer-nav.current{color:var(--accent)}
.footer-divider{left:191px;top:2754px;width:801px;height:1px;background:var(--navy-line)}
.footer-head{top:2775px;font-size:15px;color:#fff;font-weight:400;padding-bottom:4px;border-bottom:1px solid var(--accent)}
.field{border:1px solid var(--navy-line);color:#c9cad3;font-size:9.5px;padding:8px 9px}
.send{left:541px;top:2911px;width:30px;height:30px;border-radius:50%;background:var(--accent-soft);display:flex;align-items:center;justify-content:center}
.contact-line{left:600px;display:flex;gap:10px;color:#fff;font-size:10px;line-height:14.5px}
.contact-line svg{flex:none;margin-top:2px}
.contact-line u{text-decoration:underline}
.signature{left:806px;top:2775px;width:186px;height:56px;background:linear-gradient(90deg,rgba(255,255,255,0),rgba(255,255,255,.06),rgba(255,255,255,0))}
.socials{left:852px;top:2895px;display:flex;gap:9px}
.social{width:29px;height:29px;border:1px solid #7c7f92;display:flex;align-items:center;justify-content:center}
.social.active{background:var(--accent-soft);border-color:var(--accent-soft)}
.social i{display:block;width:7px;height:7px;background:#fff}
.social.active i{background:var(--navy)}
.chat{left:1104px;top:2940px;width:29px;height:31px;background:var(--accent-soft);display:flex;align-items:center;justify-content:center}
.copyright{left:191px;top:2972px;font-size:8.6px;color:#fff}
.copyright u{text-decoration:underline}
</style>
</head>
<body>

<!-- header -->
<header>
  <div class="abs brand"><span class="brand-square"></span>Mireval Stone Development</div>
  <a class="abs nav current" style="left:651px">HOME</a>
  <a class="abs nav nav-link" style="left:727px">ABOUT US</a>
  <a class="abs nav nav-link" style="left:820px">NEWS</a>
  <a class="abs btn-dark">CONTACT US</a>
</header>

<!-- hero -->
<section>
  <div class="abs hero" role="img" aria-label="Modern two-storey house with dark timber facade at dusk, lawn and stone steps framed by trees"></div>
  <div class="abs hero-shade"></div>
  <div class="abs hero-frame"></div>
  <div class="abs hero-mark"></div>
  <h1 class="abs hero-title">A Growing real estate development company specializing in multi-family apartment development.</h1>
  <a class="abs btn-ghost hero-btn">CONTACT US</a>
  <svg class="abs scroll-arrow" width="14" height="20" viewBox="0 0 14 20"><path d="M7 1v17M2 13l5 5 5-5" fill="none" stroke="#fff" stroke-width="1.3"/></svg>
</section>

<!-- about -->
<section>
  <div class="abs label-line" style="top:733px"></div>
  <div class="abs label" style="top:725px">About Us</div>
  <h2 class="abs heading" style="top:750px">Welcome to the<br>Mireval Stone Development</h2>
  <div class="abs about-rule"></div>
  <div class="abs about-copy">
    <p><strong>Mireval Stone Development</strong> was created to satisfy the overwhelming request to help our clients who want to invest in long term buy and hold Real Estate, and create a more profitable and balanced investment portfolio. We offer opportunities to invest in cash flowing Multi-Family apartment building investments in the Southern California area.</p>
    <p>"Many of our clients are looking to diversify their retirement portfolio, but don't know the ins and outs of how to invest in Managed Real Estate investments."</p>
  </div>
  <a class="abs btn-ghost btn-outline about-btn">LEARN MORE</a>
  <div class="abs about-photo" role="img" aria-label="Contemporary home terrace at night with fire pit and lounge seating under a deep blue sky"></div>
  <div class="abs about-inset"></div>
  <div class="abs about-tail"></div>
</section>

<!-- stats -->
<section>
  <div class="abs stats-photo" role="img" aria-label="Multi-level modern residence with glass balconies at sunset beside pine trees"></div>
  <div class="abs stats-panel">
    <div class="stat"><span class="stat-num">02</span><span class="stat-label">Partners</span></div>
    <div class="stat"><span class="stat-num">06</span><span class="stat-label">Employees</span></div>
    <div class="stat"><span class="stat-num">33</span><span class="stat-label">Investments</span></div>
    <div class="stat"><span class="stat-num">100%</span><span class="stat-label">Success</span></div>
  </div>
</section>

<!-- industry -->
<section>
  <div class="abs label-line" style="top:1760px"></div>
  <div class="abs label" style="top:1752px">Industry</div>
  <h2 class="abs heading" style="top:1778px">Committed to the fundamentals of investing,<br>to ensure longterm growth</h2>
  <article class="abs card card-1" role="img" aria-label="Architect studying a scale model of an apartment tower">
    <div class="card-shade"></div><span class="card-num">01.</span><h3 class="card-title">Apartment Building<br>Optimization</h3>
  </article>
  <article class="abs card card-2" role="img" aria-label="Two colleagues reviewing property documents at a desk">
    <div class="card-shade"></div><span class="card-num">02.</span><h3 class="card-title">Real Estate Portfolio<br>Management</h3>
  </article>
  <article class="abs card card-3" role="img" aria-label="Handshake over signed lending paperwork">
    <div class="card-shade"></div><span class="card-num">03.</span><h3 class="card-title">Private<br>Lending</h3>
  </article>
  <div class="abs card-tail"></div>
</section>

<!-- properties -->
<section>
  <div class="abs props-bg"></div>
  <div class="abs label-line" style="top:2241px"></div>
  <div class="abs label" style="top:2233px">Properties</div>
  <h2 class="abs heading" style="top:2258px">Current Offered Properties</h2>
  <div class="abs prop-photo" role="img" aria-label="Offered property: modern home terrace at night with fire pit and outdoor lounge"></div>
  <h3 class="abs prop-title">Bold and Breathtaking</h3>
  <p class="abs prop-desc">Designed and Constructed by International Asset Developer Dorian Hale Vasquez.</p>
  <div class="abs specs">
    <div class="spec"><i class="spec-icon"></i><span>BEDROOM</span><span>3</span></div>
    <div class="spec"><i class="spec-icon"></i><span>BATHS</span><span>2.5</span></div>
    <div class="spec"><i class="spec-icon"></i><span>AREA</span><span>2,136 SQ FT.</span></div>
    <div class="spec"><i class="spec-icon"></i><span>PARKING</span><span>1</span></div>
  </div>
  <div class="abs offered">Offered at:<span class="price">$2,499,000</span></div>
  <a class="abs btn-ghost btn-outline prop-btn">LEARN MORE</a>
  <div class="abs prop-rule"></div>
</section>

<!-- footer -->
<footer>
  <div class="abs footer"></div>
  <div class="abs footer-sky"></div>
  <div class="abs footer-mark"></div>
  <a class="abs footer-nav current" style="left:646px">HOME</a>
  <a class="abs footer-nav" style="left:734px">ABOUT US</a>
  <a class="abs footer-nav" style="left:841px">NEWS</a>
  <a class="abs footer-nav" style="left:928px">CONTACT US</a>
  <div class="abs footer-divider"></div>

  <h4 class="abs footer-head" style="left:191px">Send Us a Message</h4>
  <div class="abs field" style="left:191px;top:2822px;width:185px;height:29px">Name</div>
  <div class="abs field" style="left:395px;top:2822px;width:185px;height:29px">Email</div>
  <div class="abs field" style="left:191px;top:2864px;width:389px;height:62px">Message...</div>
  <div class="abs send"><svg width="13" height="13" viewBox="0 0 14 14"><path d="M13 1L1 6l5 2 2 5z M6 8l7-7" fill="none" stroke="#23263a" stroke-width="1.1" stroke-linejoin="round"/></svg></div>

  <h4 class="abs footer-head" style="left:600px">Contact Info</h4>
  <div class="abs contact-line" style="top:2823px">
    <svg width="10" height="12" viewBox="0 0 10 12"><path d="M5 11S1 7 1 4.5a4 4 0 018 0C9 7 5 11 5 11z" fill="none" stroke="#c4a4a8"/><circle cx="5" cy="4.5" r="1.3" fill="#c4a4a8"/></svg>
    <span>1840 Harbor Crest Ave,<br>Suite 310, Del Mar,<br>CA. 92014</span>
  </div>
  <div class="abs contact-line" style="top:2880px">
    <svg width="11" height="11" viewBox="0 0 11 11"><path d="M2 1l2 2-1 1.5c.7 1.4 1.9 2.6 3.5 3.5L8 7l2 2-1.5 1.5C5 10 1 6 .5 2.5z" fill="none" stroke="#c4a4a8"/></svg>
    <u>(555) 014-2290</u>
  </div>
  <div class="abs contact-line" style="top:2912px">
    <svg width="11" height="10" viewBox="0 0 11 10"><rect x=".5" y="1" width="10" height="8" fill="none" stroke="#c4a4a8"/><path d="M.5 1l5 4 5-4" fill="none" stroke="#c4a4a8"/></svg>
    <span>hello@mirevalstone.com</span>
  </div>

  <div class="abs signature" role="img" aria-label="Handwritten signature of the company principal"></div>
  <div class="abs socials">
    <span class="social"><i></i></span>
    <span class="social active"><i></i></span>
    <span class="social"><i></i></span>
    <span class="social"><i></i></span>
  </div>
  <div class="abs chat"><svg width="14" height="12" viewBox="0 0 14 12"><rect x=".5" y=".5" width="13" height="9" fill="none" stroke="#fff"/><path d="M3 4h8M3 6.5h6" stroke="#fff"/></svg></div>
  <p class="abs copyright">Copyright @ 2024 <u>Mireval Stone Development</u>. All Rights Reserved.</p>
</footer>

</body>
</html>
```